Need a stunning looking Business Card Design for my Telecom Business, Wow FACTOR!

I deal with high level IT Directors , and Contractors.
I need to impress them with a sleek , professional and unique business card.
Im thinking options as far as rounded edges, plastic , or even metal card or die cut on a corner.
Whatever looks better and leave an unforgettable first impression.
im looking for the wow factor.
Front should have the basics info (attached on the picture of current business card)
i would like to add picture of myself somewhere
Back side
should have logo and maybe some pictures or past projects, you can download from my website ( www.lumvexholdings.com)

```html
<!DOCTYPE html>
<html lang="en">
<head>
<meta charset="utf-8">
<title>Lumvex Holdings – Business Card</title>
<link href="https://fonts.googleapis.com/css2?family=Red+Hat+Display:wght@500;700&display=swap" rel="stylesheet">
<style>
  :root {
    --page: #ffffff;
    --card: #ffffff;
    --brand-blue: #1f8ac4;
    --link-blue: #2a9fd6;
    --ink-dark: #1b1f2a;
    --grey: #8d8f94;
    --divider: #1a6fb0;
    --photo-warm: #e9b98f;
    --photo-cool: #8f929a;
  }
  html, body {
    margin: 0;
    padding: 0;
    width: 1200px;
    height: 1200px;
    overflow: hidden;
    background: var(--page);
    font-family: "Red Hat Display", Arial, sans-serif;
  }
  .canvas {
    position: relative;
    width: 1200px;
    height: 1200px;
  }
  .card {
    position: absolute;
    left: 300px;
    width: 600px;
    height: 343px;
    background: var(--card);
    box-shadow: 0 4px 8px rgba(0, 0, 0, 0.28);
  }
  .card--back { top: 204px; }
  .card--front { top: 656px; height: 340px; }

  /* Back side */
  .brand {
    position: absolute;
    left: 0;
    right: 0;
    top: 118px;
    display: flex;
    align-items: center;
    justify-content: center;
    gap: 12px;
  }
  .brand__dot {
    width: 18px;
    height: 18px;
    border-radius: 50%;
    background: var(--brand-blue);
  }
  .brand__name {
    font-weight: 700;
    font-size: 26px;
    letter-spacing: 2px;
    color: var(--ink-dark);
    text-transform: uppercase;
  }
  .back__url {
    position: absolute;
    left: 0;
    right: 0;
    top: 280px;
    text-align: center;
    font-weight: 700;
    font-size: 13px;
    color: var(--link-blue);
  }

  /* Front side */
  .portrait {
    position: absolute;
    left: 40px;
    top: 58px;
    width: 138px;
    height: 138px;
    border-radius: 50%;
    background: linear-gradient(160deg, #1d4f86, #2aa3dc);
    padding: 3px;
    box-sizing: border-box;
  }
  .portrait__inner {
    width: 100%;
    height: 100%;
    border-radius: 50%;
    background: #fff;
    padding: 5px;
    box-sizing: border-box;
  }
  .portrait__photo {
    width: 100%;
    height: 100%;
    border-radius: 50%;
    background: linear-gradient(180deg, var(--photo-warm) 0%, #d9c0a6 50%, var(--photo-cool) 100%);
  }
  .identity {
    position: absolute;
    right: 30px;
    top: 52px;
    text-align: right;
  }
  .identity__name {
    margin: 0;
    font-weight: 700;
    font-size: 24px;
    color: var(--brand-blue);
    line-height: 1.1;
  }
  .identity__title {
    margin: 4px 0 0;
    font-weight: 500;
    font-size: 16px;
    color: var(--grey);
  }
  .about, .contact {
    position: absolute;
    top: 238px;
    margin: 0;
    font-weight: 500;
    font-size: 13px;
    line-height: 19px;
    color: var(--grey);
  }
  .about { left: 42px; }
  .contact { right: 30px; text-align: right; }
  .divider {
    position: absolute;
    left: 299px;
    top: 244px;
    width: 2px;
    height: 48px;
    background: var(--divider);
  }
</style>
</head>
<body>
<main class="canvas">
  <section class="card card--back" aria-label="Card back">
    <div class="brand">
      <span class="brand__dot"></span>
      <span class="brand__name">Lumvex Holdings</span>
    </div>
    <p class="back__url">www.lumvexholdings.com</p>
  </section>

  <section class="card card--front" aria-label="Card front">
    <div class="portrait">
      <div class="portrait__inner">
        <div class="portrait__photo" role="img" aria-label="Portrait photo of the operations manager"></div>
      </div>
    </div>
    <div class="identity">
      <h1 class="identity__name">Daniel Orvane</h1>
      <p class="identity__title">Operations Manager</p>
    </div>
    <p class="about">Low Voltage Contractor<br>Offices in miami, Broward<br>and Plam Beach</p>
    <div class="divider"></div>
    <p class="contact">954 555-0142<br>info@lumvexholdings.com<br>www.lumvexholdings.com</p>
  </section>
</main>
</body>
</html>
```